Commercial facility maintenance

I need a card design that helps my salesmen make contact with new clients, our product is facility maintenance and heavy industrial maintenance

```html
<!DOCTYPE html>
<html lang="en">
<head>
<meta charset="utf-8">
<title>Harrow Ironworks LLC – Business Card</title>
<link rel="stylesheet" href="https://fonts.googleapis.com/css2?family=Archivo+Black&family=Saira:wght@400;500;600&family=Tinos:wght@700&display=swap">
<style>
  :root {
    --stage: #2b2b2d;
    --brand-red: #a3212b;
    --brand-red-dark: #6e1c22;
    --ink: #2f2f33;
    --ink-soft: #4a4a4f;
    --rule: #6b6b70;
    --paper: #ffffff;
    --silver: #c9c9cc;
  }
  * { box-sizing: border-box; margin: 0; padding: 0; }
  html, body {
    width: 1200px; height: 689px; overflow: hidden;
    background: var(--stage);
  }
  .stage {
    width: 1200px; height: 689px;
    display: flex; align-items: center; justify-content: center; gap: 40px;
  }
  .card {
    position: relative;
    width: 540px; height: 309px;
    border-radius: 18px;
    overflow: hidden;
    box-shadow: 0 18px 40px rgba(0,0,0,.45);
  }

  /* Back side */
  .card--back { background: var(--brand-red); }
  .back-pattern {
    position: absolute; inset: 0;
    background: linear-gradient(120deg, var(--brand-red) 0%, #8e2029 55%, var(--brand-red-dark) 100%);
  }
  .back-identity {
    position: absolute; left: 0; right: 0; top: 50%;
    transform: translateY(-50%);
    text-align: center;
  }
  .back-name {
    font-family: "Archivo Black", sans-serif;
    font-size: 27px; letter-spacing: 1px;
    color: var(--paper);
  }
  .back-tagline {
    margin-top: 6px;
    font-family: "Saira", sans-serif;
    font-size: 12px; font-weight: 500; letter-spacing: 2.5px;
    color: var(--silver);
  }

  /* Front side */
  .card--front { background: var(--paper); }
  .front-mark {
    position: absolute; left: 28px; top: 80px;
    width: 200px; height: 120px;
    display: flex; align-items: center; gap: 10px;
  }
  .mark-dot {
    flex: none; width: 18px; height: 18px; border-radius: 50%;
    background: var(--brand-red);
  }
  .mark-name {
    font-family: "Saira", sans-serif; font-weight: 600;
    font-size: 20px; line-height: 1.15; letter-spacing: 1px;
    color: var(--ink);
  }
  .front-divider {
    position: absolute; left: 246px; top: 52px;
    width: 1px; height: 150px; background: var(--rule);
  }
  .front-details {
    position: absolute; left: 266px; top: 42px; right: 20px;
  }
  .person-name {
    font-family: "Tinos", serif; font-weight: 700;
    font-size: 30px; letter-spacing: 1px; color: var(--ink);
  }
  .person-role {
    font-family: "Saira", sans-serif; font-size: 14px;
    color: var(--brand-red); margin: 0 0 10px;
  }
  .contact-list { list-style: none; }
  .contact-item {
    display: flex; align-items: flex-start; gap: 8px;
    font-family: "Saira", sans-serif; font-size: 12px; line-height: 1.35;
    color: var(--ink-soft); margin-bottom: 3px;
  }
  .contact-icon { flex: none; width: 11px; height: 11px; margin-top: 3px; fill: var(--brand-red); }
  .front-band {
    position: absolute; left: 0; right: 0; bottom: 0; height: 48px;
    background: var(--brand-red);
    border-top: 5px solid var(--paper);
    box-shadow: 0 -2px 0 var(--rule);
    display: flex; align-items: center; justify-content: center;
  }
  .band-tagline {
    font-family: "Saira", sans-serif; font-size: 12.5px; font-weight: 500;
    letter-spacing: 1.2px; color: var(--paper);
  }
</style>
</head>
<body>
<main class="stage">
  <section class="card card--back">
    <div class="back-pattern" role="img" aria-label="Repeating pattern of the company emblem on red"></div>
    <div class="back-identity">
      <p class="back-name">HARROW IRONWORKS LLC</p>
      <p class="back-tagline">PRECISION. PUNCTUALITY. PROFESSIONALISM</p>
    </div>
  </section>

  <section class="card card--front">
    <div class="front-mark">
      <span class="mark-dot"></span>
      <span class="mark-name">HARROW<br>IRONWORKS LLC</span>
    </div>
    <div class="front-divider"></div>
    <div class="front-details">
      <h1 class="person-name">DANIEL REYES</h1>
      <p class="person-role">Founder &amp; CEO</p>
      <ul class="contact-list">
        <li class="contact-item">
          <svg class="contact-icon" viewBox="0 0 12 12"><path d="M6 0a4 4 0 0 0-4 4c0 3 4 8 4 8s4-5 4-8a4 4 0 0 0-4-4zm0 5.5A1.5 1.5 0 1 1 6 2.5a1.5 1.5 0 0 1 0 3z"/></svg>
          <span>Harrow Ironworks LLC<br>Your Street Address Here, City<br>State, Country, ZIP 123</span>
        </li>
        <li class="contact-item">
          <svg class="contact-icon" viewBox="0 0 12 12"><path d="M2.5 0l2 3-1.2 1.3a7 7 0 0 0 4.4 4.4L9 7.5l3 2-1 2.2C5 12 0 7 .3 1z"/></svg>
          <span>555-010-2244</span>
        </li>
        <li class="contact-item">
          <svg class="contact-icon" viewBox="0 0 12 12"><path d="M0 2h12v8H0z M0 2l6 4 6-4" stroke="#fff" stroke-width=".8"/></svg>
          <span>info@harrowironworks.com</span>
        </li>
        <li class="contact-item">
          <svg class="contact-icon" viewBox="0 0 12 12"><circle cx="6" cy="6" r="6"/><path d="M0 6h12M6 0c-3 3-3 9 0 12M6 0c3 3 3 9 0 12" stroke="#fff" stroke-width=".8" fill="none"/></svg>
          <span>harrowironworks.com</span>
        </li>
      </ul>
    </div>
    <div class="front-band">
      <p class="band-tagline">PRECISION. EXPERIENCE. MECHANICAL SOLUTIONS THAT LAST.</p>
    </div>
  </section>
</main>
</body>
</html>
```